Technology research organisation needs a white paper redesign

Goal: Redesign the current "Platform Choosing" white paper using our Telmora Analytics branding.
- The design should promote a brand which is independent, has trusted advisors, is down to earth, has plain english advice based on solid research.
- Prefer a one column layout which is easy to read and has enough space for call outs on either left or right hand side.
- A4 size document will be distributed in PDF format
- Feel free to re-design existing graphs, tables, change images, headers and footers.
- Audience: HR Directors, CIO's & CFO's
- Must use our standard colour palette, see attached.
- The font used is company name: Frutiger LT 57 CN
- Should be inline with our website: telmoraanalytics.com.au
Design must allow for:
* Front Page
* Main content
* Contact details, about Telmora Analytics & author example content can be found http://telmoraanalytics.com.au/about/
Output:
- All adobe design files
- Images, Fonts
Target Market(s)
Audience: HR Directors, CIO's & CFO's most likely 40+
Industry/Entity Type
It Company
Font styles to use
Other font styles liked:
- Frutiger LT 57 CN
Look and feel

```html
<!DOCTYPE html>
<html lang="en">
<head>
<meta charset="utf-8">
<title>Telmora Analytics – Platform Choosing white paper spreads</title>
<link rel="stylesheet" href="https://fonts.googleapis.com/css2?family=PT+Sans:ital,wght@0,400;0,700;1,400;1,700&display=swap">
<style>
  :root {
    --ink: #333333;
    --charcoal: #363636;
    --heading-grey: #bdbdbd;
    --square-grey: #c4c4c4;
    --body: #3a3a3a;
    --red: #e8392a;
    --sand: #e3d9a1;
    --sand-text: #e4dca6;
    --lime: #c9d62f;
    --lime-text: #c5d33a;
    --paper: #ffffff;
    --edge: #dcdcdc;
    --faint: #f4f4f4;
  }
  * { box-sizing: border-box; margin: 0; padding: 0; }
  html, body { width: 855px; height: 1200px; overflow: hidden; background: #ffffff; }
  body { position: relative; font-family: "PT Sans", Arial, sans-serif; color: var(--body); }

  .spread {
    position: absolute; left: 29px; width: 795px; height: 564px;
    display: flex; background: var(--paper);
    box-shadow: 1px 2px 6px rgba(0,0,0,0.18);
    border: 1px solid var(--edge);
  }
  .spread--top { top: 27px; }
  .spread--bottom { top: 608px; }

  .page { position: relative; width: 50%; height: 100%; }
  .page + .page { border-left: 1px solid #e6e6e6; }
  .page--dark { background: var(--charcoal); }

  .statement {
    position: absolute; top: 112px; right: 40px; text-align: right;
    color: #ffffff; font-size: 32px; line-height: 47px; letter-spacing: 0.5px;
    text-transform: uppercase;
  }

  .section-title {
    position: absolute; top: 32px; font-size: 25px; line-height: 29px;
    font-weight: 700; color: var(--heading-grey); text-transform: uppercase; letter-spacing: 0.2px;
  }
  .section-title--left { left: 40px; }
  .section-title--right { right: 39px; text-align: right; }

  .square { position: absolute; display: block; }
  .square--sand { background: var(--sand); }
  .square--grey { background: var(--square-grey); }
  .square--charcoal { background: var(--ink); }
  .square--red { background: var(--red); }
  .square--lime { background: var(--lime); }

  .body-copy {
    position: absolute; top: 116px; font-size: 7.4px; line-height: 15px;
    text-align: justify; color: var(--body); letter-spacing: 0.15px;
  }
  .body-copy p + p { margin-top: 6px; }
  .body-copy--right { left: 40px; width: 250px; }
  .body-copy--left { left: 108px; width: 249px; }

  .callout {
    position: absolute; top: 351px; left: 40px; width: 310px;
    font-style: italic; font-size: 12.5px; line-height: 18px; color: var(--sand-text);
  }
  .callout span { display: block; }
  .callout .indent { padding-left: 50px; }
  .callout strong { font-weight: 700; }

  .quote {
    position: absolute; top: 116px; left: 40px; width: 307px;
    font-size: 16.5px; line-height: 25.5px; color: var(--lime-text); letter-spacing: 0.6px;
  }
  .quote-author {
    position: absolute; top: 234px; right: 50px;
    font-style: italic; font-weight: 700; font-size: 16.5px; color: var(--lime-text);
  }
  .decor-mark {
    position: absolute; left: 150px; top: 343px; width: 84px; height: 96px;
    background: var(--faint); border-radius: 42px;
  }

  .page-footer { position: absolute; top: 518px; width: 308px; }
  .page-footer--right { left: 40px; }
  .page-footer--left { left: 50px; text-align: right; }
  .brand { font-size: 7.5px; font-weight: 700; color: var(--ink); letter-spacing: 0.3px; text-transform: uppercase; }
  .brand em { font-style: normal; color: var(--red); }
  .rule { height: 1px; background: var(--red); margin-top: 3px; }
  .footer-line {
    display: flex; justify-content: space-between; margin-top: 4px;
    font-size: 7px; letter-spacing: 0.4px; color: var(--ink); text-transform: uppercase;
  }
  .folio { font-weight: 700; }
</style>
</head>
<body>

<section class="spread spread--top">
  <div class="page page--dark">
    <p class="statement">Nearly 60%<br>of HR systems<br>in Australia<br>have been<br>in use for<br>over 5 years</p>
  </div>
  <div class="page">
    <h2 class="section-title section-title--left">HR investment in<br>technology</h2>
    <span class="square square--sand" style="left:305px;top:25px;width:31px;height:31px"></span>
    <span class="square square--grey" style="left:349px;top:48px;width:31px;height:31px"></span>
    <span class="square square--charcoal" style="left:289px;top:63px;width:23px;height:23px"></span>
    <span class="square square--red" style="left:326px;top:68px;width:10px;height:10px"></span>

    <div class="body-copy body-copy--right">
      <p>HR practitioners are telling us their primary motivation for investing in HR Technology is improved operational efficiency and reducing operational costs/headcount.</p>
      <p>Unfortunately these same HR professionals are reporting that gaining access to the appropriate budget is the number one roadblock for utilising better solutions.</p>
      <p>Today's HR/Payroll departments need technology solutions that deliver functional, sustainable and compliant environment to meet both the current and future business growth.</p>
      <p>Many of today's systems in use in Australia are unable to help HR deliver streamlined processes in an efficient and effective manner.</p>
    </div>

    <p class="callout">
      <span>When it comes to HR Technology investments</span>
      <span class="indent">HR/Payroll teams are in the <strong>perfect storm</strong>.</span>
    </p>

    <footer class="page-footer page-footer--right">
      <div class="brand"><em>Telmora</em> Analytics</div>
      <div class="rule"></div>
      <div class="footer-line"><span>Market intelligence &amp; advisory</span><span class="folio">5</span></div>
    </footer>
  </div>
</section>

<section class="spread spread--bottom">
  <div class="page">
    <span class="square square--grey" style="left:16px;top:45px;width:31px;height:31px"></span>
    <span class="square square--lime" style="left:60px;top:23px;width:31px;height:31px"></span>
    <span class="square square--red" style="left:59px;top:65px;width:10px;height:10px"></span>
    <span class="square square--charcoal" style="left:83px;top:61px;width:23px;height:23px"></span>
    <h2 class="section-title section-title--right">Navigating the HR<br>tech market</h2>

    <div class="body-copy body-copy--left">
      <p>Telmora Analytics currently tracks over 200 vendors who deliver services to the Australian marketplace.</p>
      <p>With so many vendors—many offering similar features—it is hard for organisations to determine which vendors are the perfect fit.</p>
      <p>It is common for the person placed in charge of this selection process to have not done it before.</p>
      <p>Today's HR professional are not technologists. There is a lot of marketing hype, with confusing terminology and various options. To be successful you need to get through to the heart of the solution—how will the technology platform help you.</p>
      <p>For many HR organisations the purchasing of a new HR/Payroll solution is one of the largest expenses they undertake, other than managing the organisation's payroll! This last fact will ensure oversight from your CFO on any purchase.</p>
    </div>

    <footer class="page-footer page-footer--left">
      <div class="brand"><em>Telmora</em> Analytics</div>
      <div class="rule"></div>
      <div class="footer-line"><span class="folio">6</span><span>Market intelligence &amp; advisory</span></div>
    </footer>
  </div>
  <div class="page">
    <p class="quote">If you look at the various strategies available for dealing with new tech-nology, sticking your head in the sand is not the most plausible strategy.</p>
    <p class="quote-author">–Edwin Hallorant</p>
    <div class="decor-mark" role="img" aria-label="Faint brand decoration mark"></div>
  </div>
</section>

</body>
</html>
```